New letterhead/ stationary design for insurance restoration builder

Modern, clever creative not cheap tacky design maroon and black / white are logo colours. Company name is Pillar Rock Building Services. Might need two different versions of new design, one for standard letterhead communicatio, the other i need to use for management aystems policies amd procedirrs etc.becauuse you wong have tome
Target Market(s)
Large residential insurance companies and their clients, tradespeople and the integrated management system with policies and procedures is internal company employees.
Requirements
Must have
- A version that would be used as a typical business letterhead is and the other needs to be in a format / design that suits company policies and procedures. Be professional, PILLAR and be creative / totally custom for pur business not just an edited version of what you can get for free in Word or off the internet pls. Incorporating industry relevant shapes or placement to create the illusion of a residential construction related image is an idea. Someone who is cleverly creative with simple but impactdul design will get my interest.
Nice to have
- Can have different shades of the corporate colours used which are maroon / burgundy and black. https://qvimagehost.net/common/images/v3/sketch-icon-dropzone.png
Should not have
- Look like the genetic templates and designs you can do yourself copying off the internet.

```html
<!DOCTYPE html>
<html lang="en">
<head>
<meta charset="utf-8">
<title>Pillar Rock Building Services – Letterhead</title>
<link href="https://fonts.googleapis.com/css2?family=Lato:ital,wght@0,400;0,700;0,900;1,400;1,700&display=swap" rel="stylesheet">
<style>
  :root {
    --maroon: #9a1b38;
    --maroon-deep: #8c1833;
    --dimension: #e46a8a;
    --paper: #ffffff;
    --ink: #333333;
    --body: #6a6a6a;
    --bar: #111111;
  }
  * { margin: 0; padding: 0; box-sizing: border-box; }
  html, body { width: 927px; height: 1200px; overflow: hidden; background: var(--maroon); }
  .canvas { position: relative; width: 927px; height: 1200px; font-family: "Lato", Arial, sans-serif; }
  .backdrop { position: absolute; inset: 0; }
  .dimension-label { font-family: "Lato", Arial, sans-serif; font-size: 9px; fill: var(--dimension); }

  .brand-name {
    position: absolute; left: 141px; top: 178px; width: 645px;
    font-weight: 900; font-size: 40px; line-height: 1; letter-spacing: -0.5px;
    color: var(--maroon);
  }
  .brand-bar {
    position: absolute; left: 141px; top: 247px; width: 645px; height: 23px;
    background: var(--bar);
  }
  .letter-date {
    position: absolute; right: 18px; top: 4px;
    font-size: 14px; font-style: italic; font-weight: 700; letter-spacing: 2px;
    color: var(--paper);
  }

  .greeting {
    position: absolute; left: 141px; top: 352px;
    font-size: 20px; font-weight: 700; color: var(--ink);
  }
  .letter-body { position: absolute; left: 141px; top: 399px; width: 645px; }
  .letter-body p {
    font-size: 15.4px; line-height: 23.8px; color: var(--body);
    text-align: justify; margin-bottom: 23.8px;
  }

  .sign-off { position: absolute; left: 141px; top: 815px; font-size: 20px; font-weight: 700; color: var(--ink); }
  .signatory { position: absolute; left: 141px; top: 869px; font-size: 20px; font-weight: 700; color: var(--ink); }
  .signatory-role { position: absolute; left: 141px; top: 899px; font-size: 11px; font-style: italic; font-weight: 700; color: #555; }

  .contact-rule { position: absolute; left: 141px; top: 1056px; width: 645px; height: 3px; background: var(--maroon); }
  .contact-line {
    position: absolute; left: 141px; top: 1069px; width: 645px;
    display: flex; font-size: 16px; letter-spacing: 1px; color: var(--maroon);
  }
  .contact-email { width: 278px; }
  .contact-phone { flex: 1; }
</style>
</head>
<body>
<div class="canvas">
  <svg class="backdrop" width="927" height="1200" viewBox="0 0 927 1200" aria-hidden="true">
    <rect width="927" height="1200" fill="var(--maroon)"/>
    <polygon points="56,55 697,55 873,235 873,1144 56,1144" fill="var(--paper)"/>
    <g stroke="var(--dimension)" stroke-width="1" fill="none">
      <line x1="30" y1="57" x2="30" y2="272"/>
      <polyline points="26,62 30,56 34,62"/><polyline points="26,266 30,272 34,266"/>
      <line x1="730" y1="57" x2="873" y2="200"/>
      <polyline points="731,64 729,56 737,58"/><polyline points="866,198 874,200 872,192"/>
      <line x1="903" y1="237" x2="903" y2="1018"/>
      <polyline points="899,243 903,237 907,243"/><polyline points="899,1012 903,1018 907,1012"/>
      <line x1="903" y1="1040" x2="903" y2="1140"/>
      <polyline points="899,1046 903,1040 907,1046"/><polyline points="899,1134 903,1140 907,1134"/>
      <line x1="58" y1="1171" x2="871" y2="1171"/>
      <polyline points="64,1167 58,1171 64,1175"/><polyline points="865,1167 871,1171 865,1175"/>
    </g>
    <text class="dimension-label" x="12" y="165">140</text>
    <text class="dimension-label" x="804" y="118" transform="rotate(45 804 118)">140</text>
    <text class="dimension-label" x="898" y="692">435</text>
    <text class="dimension-label" x="900" y="1084">20</text>
    <text class="dimension-label" x="455" y="1183">540</text>
  </svg>

  <div class="brand-name">Pillar Rock Building Services</div>
  <div class="brand-bar"><span class="letter-date">December 07, 2020</span></div>

  <p class="greeting">Dear Mr. Johnathan Doe,</p>

  <div class="letter-body">
    <p>Lorem ipsum dolor sit amet, consectetuer adipiscing elit, sed diam nonummy nibh euismod tincidunt ut laoreet dolore magna aliquam erat volutpat. Ut wisi enim adn vulero eros et accumsan et iusto odio dignissim qui blandit praesent luptatum zzril delenit augue duis dolore te feugait nulla facilisi.</p>
    <p>Lorem ipsum dolor sit amet, cons ectetuer adipiscing elit, sed diam nonummy nibh euismdipiscing elit, sed diam nonummy nibh euismod tincidunt ut laoreet dolore magna aliquam erat volutpat. Ut wisi enim ad minim veniam, quis nostrud exerci tation ullamcorper suscipit lobortis nisl ut aliquip ex ea commodo consequat. Duis ea commodo consequat</p>
    <p>Lorem ipsum dolor sit amet, consectetuer adipiscing elit, sed diam nonummy nibh euismod tincidunt ut laoreet dolore magna aliquam erat volutpat. Ut wisi enim ad zzril delenit augue duis dolore te feugait nulla facilisi.</p>
  </div>

  <p class="sign-off">Sincerely,</p>
  <p class="signatory">Daniel Marsh</p>
  <p class="signatory-role">Chief Exective Officer</p>

  <div class="contact-rule"></div>
  <div class="contact-line">
    <span class="contact-email">info@pillarrockbuilding.com.au</span>
    <span class="contact-phone">03 9000 4821</span>
    <span class="contact-web">pillarrockbuilding.com.au</span>
  </div>
</div>
</body>
</html>
```